Business Card Design Project

Need a business card with logo that is attached.
Company name: Tolmen Brisk Solutions, LLC
My name: Lorna Tolmen
Title: President
Phone number: 703-555-0148
Email: ltolmen@tolmenbrisksolutions.example
web site: www.tolmenbrisksolutions.example

Industry/Entity Type

Business

```html
<!DOCTYPE html>
<html lang="en">
<head>
<meta charset="utf-8">
<title>Tolmen Brisk Solutions, LLC – Business Card</title>
<link rel="stylesheet" href="https://fonts.googleapis.com/css2?family=Alegreya:wght@400;500&display=swap">
<style>
  :root {
    --navy: #27347f;
    --blue: #2a63b8;
    --sky: #2b93d6;
    --teal: #1f8e78;
    --green: #2f9a78;
    --paper: #ffffff;
    --stage: #e9eaec;
    --shadow: rgba(20, 25, 40, 0.18);
  }
  * { box-sizing: border-box; margin: 0; padding: 0; }
  html, body { width: 1200px; height: 926px; overflow: hidden; }
  body {
    background: var(--stage);
    font-family: "Alegreya", Georgia, serif;
    position: relative;
  }
  .card {
    position: absolute;
    left: 250px;
    width: 700px;
    height: 400px;
    background: var(--paper);
    box-shadow: 0 6px 18px var(--shadow);
    overflow: hidden;
  }
  .card--back { top: 42px; }
  .card--front { top: 484px; }

  /* Back face */
  .back-brand {
    position: absolute;
    inset: 0;
    display: flex;
    align-items: center;
    justify-content: center;
    gap: 18px;
  }
  .brand-dot {
    border-radius: 50%;
    background: var(--blue);
    flex: none;
  }
  .back-brand .brand-dot { width: 86px; height: 86px; }
  .brand-name {
    color: var(--blue);
    font-weight: 400;
    text-transform: uppercase;
    line-height: 1.05;
    letter-spacing: 0.02em;
  }
  .back-brand .brand-name { font-size: 30px; }

  /* Front face */
  .front-art { position: absolute; inset: 0; }
  .front-brand {
    position: absolute;
    left: 44px;
    top: 38px;
    display: flex;
    align-items: center;
    gap: 14px;
  }
  .front-brand .brand-dot { width: 64px; height: 64px; }
  .front-brand .brand-name { font-size: 21px; }

  .person {
    position: absolute;
    right: 44px;
    top: 48px;
    text-align: right;
  }
  .person-name {
    color: var(--navy);
    font-size: 36px;
    font-weight: 500;
    line-height: 1;
  }
  .person-title {
    color: var(--green);
    font-size: 16px;
    letter-spacing: 0.18em;
    text-transform: uppercase;
    margin-top: 4px;
  }

  .contacts {
    position: absolute;
    right: 30px;
    bottom: 34px;
    list-style: none;
    display: flex;
    flex-direction: column;
    gap: 8px;
  }
  .contact {
    display: flex;
    align-items: center;
    justify-content: flex-end;
    gap: 12px;
    color: var(--navy);
    font-size: 22px;
    line-height: 1;
  }
  .contact-icon {
    width: 40px;
    height: 28px;
    background: var(--navy);
    display: flex;
    align-items: center;
    justify-content: center;
    flex: none;
  }
  .contact-icon svg { width: 18px; height: 18px; }
</style>
</head>
<body>

<section class="card card--back" aria-label="Card back">
  <div class="back-brand">
    <span class="brand-dot"></span>
    <p class="brand-name">Tolmen Brisk<br>Solutions<br>LLC</p>
  </div>
</section>

<section class="card card--front" aria-label="Card front">
  <svg class="front-art" viewBox="0 0 700 400" width="700" height="400" aria-hidden="true">
    <defs>
      <linearGradient id="edge-blue" x1="0" y1="0" x2="0.3" y2="1">
        <stop offset="0" stop-color="#2b9ad9"/>
        <stop offset="1" stop-color="#2d3f96"/>
      </linearGradient>
      <linearGradient id="edge-teal" x1="0" y1="0" x2="0" y2="1">
        <stop offset="0" stop-color="#2a9a86"/>
        <stop offset="1" stop-color="#1b7f6a"/>
      </linearGradient>
    </defs>
    <rect width="700" height="400" fill="url(#edge-blue)"/>
    <path d="M96 150 C 60 240 80 330 140 400 L 230 400 C 160 360 115 300 100 230 C 94 200 93 175 96 150 Z" fill="url(#edge-teal)"/>
    <path d="M96 150 C 60 240 80 330 140 400" fill="none" stroke="#ffffff" stroke-width="5"/>
    <path d="M122 0 C 95 80 85 160 100 230 C 115 300 160 360 230 400 L 700 400 L 700 0 Z" fill="#ffffff"/>
  </svg>

  <div class="front-brand">
    <span class="brand-dot"></span>
    <p class="brand-name">Tolmen Brisk<br>Solutions<br>LLC</p>
  </div>

  <div class="person">
    <h1 class="person-name">Lorna Tolmen</h1>
    <p class="person-title">President</p>
  </div>

  <ul class="contacts">
    <li class="contact">
      <span>703-555-0148</span>
      <span class="contact-icon">
        <svg viewBox="0 0 24 24" aria-hidden="true"><path fill="#fff" d="M6.6 10.8a15.1 15.1 0 0 0 6.6 6.6l2.2-2.2a1 1 0 0 1 1-.25 11.4 11.4 0 0 0 3.6.57 1 1 0 0 1 1 1V20a1 1 0 0 1-1 1A17 17 0 0 1 3 4a1 1 0 0 1 1-1h3.5a1 1 0 0 1 1 1c0 1.250.2 2.45.57 3.57a1 1 0 0 1-.25 1z"/></svg>
      </span>
    </li>
    <li class="contact">
      <span>www.tolmenbrisksolutions.example</span>
      <span class="contact-icon">
        <svg viewBox="0 0 24 24" aria-hidden="true"><g fill="none" stroke="#fff" stroke-width="1.8"><circle cx="12" cy="12" r="9"/><ellipse cx="12" cy="12" rx="4" ry="9"/><path d="M3 12h18"/></g></svg>
      </span>
    </li>
    <li class="contact">
      <span>ltolmen@tolmenbrisksolutions.example</span>
      <span class="contact-icon">
        <svg viewBox="0 0 24 24" aria-hidden="true"><g fill="none" stroke="#fff" stroke-width="1.8"><rect x="3" y="5" width="18" height="14"/><path d="M3 5l9 8 9-8"/></g></svg>
      </span>
    </li>
  </ul>
</section>

</body>
</html>
```